Democracy in crisis book

This book tries to sound the ALARM that we will lose our democracy unless we force Unionists to adopt the plan inside this book. I designed a mock cover (attached) but I am concerned it would not look good in the Thumbnail view that most people would see it as they're scrolling down Shopvale or Pagenook. The final title for the book is: Final Hour to Rescue the Free Republic. The current subtitle is: The Single Path to Halt the 2022 Partisan Takeover & Renew Our Homeland -- but it’s a work in progress.The subtitle is still working progress but it's really not that important and can be small.
STYLE CONSIDERATIONS:
(1) The title should be on 5 separate lines: Final; Hour; To Rescue; Free; Republic
(2) The title could be in white fat letters except for maybe one line that says “To Rescue” which could be in the blue color of the Civic Union Party-- or maybe Free Republic could be in blue. We may have to try a few variations of that.
(3) I picked the red in the mock cover to connotate an emergency,
(4) I liked big bold fat font going across the full page so that it looks like a major warning sign, though note I was unable to extend each line flush all the way to the right which I think would have been better.
(5) I liked it better flush to left instead of centered.
(6) I picked the Harwick monument + a crowd for my mock cover, but a picture of a huge crowd protesting with a picture of the United States Congress in the background would be much better. DO NOT USE HARWICK. Obviously I would need it to be an open license or something I can pay a small amount to get. If you can find that picture then the page should probably be colored in red with Congress in white.
I got the idea 4 giant title from the book “seldom a quiet so bright” and Dellowby’s “When Freedom Fades” or “Grey Herons” by Mara Vostell though I hate that font)
I love Osric Thale’s “marked since the outset” cover so if you find a picture of Congress and a protest crowd instead of painting it red you could have just a couple of jagged red stripes going across it like that cover.
I love the 3-D effect of Greta Wolven's cover for The Silverwren where it looks like a page is being ripped. That effect could be done the words Free Republic like it's being torn off the page UPDATE: MANY DESIGNERS TRIED THAT & IT DID NOT WORK AT ALL.
Note that this book will be submitted to many award competitions, so please give me an award-winning cover.
I like how the title of the book The Unchosen by Martin Fellowes has the words starting to fade. I don't like the ladder on it, but maybe 'Free Republic' could fade like that.
Unionists

```html
<!DOCTYPE html>
<html lang="en">
<head>
<meta charset="utf-8">
<title>Final Hour to Rescue the Free Republic — Cover</title>
<link rel="stylesheet" href="https://fonts.googleapis.com/css2?family=Archivo+Black&display=swap">
<style>
  :root {
    --alarm-red-deep: #960508;
    --alarm-red: #B81E22;
    --alarm-red-glow: #D8453F;
    --title-white: #FFFFFF;
    --union-blue: #42AEE6;
    --subtitle-rose: #EBBDBD;
  }
  html, body {
    margin: 0;
    padding: 0;
    width: 795px;
    height: 1200px;
    overflow: hidden;
    background: var(--alarm-red-deep);
  }
  .book-cover {
    position: relative;
    width: 795px;
    height: 1200px;
    overflow: hidden;
    font-family: "Archivo Black", "Arial Black", sans-serif;
  }
  .cover-photo {
    position: absolute;
    inset: 0;
    background:
      radial-gradient(ellipse 60% 40% at 50% 30%, rgba(232, 90, 84, 0.55), rgba(232, 90, 84, 0) 70%),
      linear-gradient(180deg, transparent 52%, rgba(240, 70, 55, 0.35) 58%, transparent 64%, rgba(240, 70, 55, 0.3) 70%, transparent 76%),
      radial-gradient(ellipse 90% 80% at 50% 45%, var(--alarm-red) 0%, var(--alarm-red) 45%, var(--alarm-red-deep) 100%);
  }
  .title-block {
    position: absolute;
    left: 0;
    top: 0;
    width: 795px;
    height: 840px;
  }
  .title-line {
    font-family: "Archivo Black", "Arial Black", sans-serif;
  }
  .subtitle {
    position: absolute;
    left: 44px;
    top: 914px;
    width: 740px;
    margin: 0;
    font-size: 39px;
    line-height: 43px;
    letter-spacing: 3px;
    white-space: nowrap;
    color: var(--subtitle-rose);
    -webkit-mask-image: linear-gradient(90deg, #000 80%, rgba(0,0,0,0.4) 100%);
            mask-image: linear-gradient(90deg, #000 80%, rgba(0,0,0,0.4) 100%);
  }
</style>
</head>
<body>
  <main class="book-cover">
    <div class="cover-photo" role="img" aria-label="Red-tinted photograph of a large protest crowd on the mall with the United States Capitol dome in the background and faint flag stripes"></div>

    <svg class="title-block" viewBox="0 0 795 840" role="heading" aria-level="1" aria-label="Final Hour to Rescue the Free Republic">
      <defs>
        <linearGradient id="fade-white" gradientUnits="userSpaceOnUse" x1="540" y1="0" x2="775" y2="0">
          <stop offset="0" stop-color="var(--title-white)" stop-opacity="1"/>
          <stop offset="1" stop-color="var(--title-white)" stop-opacity="0.15"/>
        </linearGradient>
        <linearGradient id="fade-blue" gradientUnits="userSpaceOnUse" x1="520" y1="0" x2="775" y2="0">
          <stop offset="0" stop-color="var(--union-blue)" stop-opacity="1"/>
          <stop offset="0.45" stop-color="#5E94C2" stop-opacity="0.9"/>
          <stop offset="1" stop-color="#5E6E9A" stop-opacity="0.3"/>
        </linearGradient>
      </defs>
      <text class="title-line title-final" x="44" y="306" font-size="171" fill="url(#fade-white)" textLength="722" lengthAdjust="spacing">FINAL</text>
      <text class="title-line title-hour" x="38" y="446" font-size="146" fill="url(#fade-white)" textLength="724" lengthAdjust="spacing">HOUR</text>
      <text class="title-line title-rescue" x="36" y="586" font-size="139" fill="url(#fade-blue)" textLength="726" lengthAdjust="spacingAndGlyphs">TO RESCUE</text>
      <text class="title-line title-free" x="34" y="702" font-size="114" fill="url(#fade-white)" textLength="728" lengthAdjust="spacing">FREE</text>
      <text class="title-line title-republic" x="38" y="810" font-size="97" fill="url(#fade-white)" textLength="728" lengthAdjust="spacing">REPUBLIC</text>
    </svg>

    <p class="subtitle">The Single Path to Halt the<br>2022 Partisan Takeover &amp;<br>Renew Our Homeland</p>
  </main>
</body>
</html>
```